VANTAGE Conference Retractable Standing Banner

I need a design for a 32X80 in retractable banner for a conference. The full title of the conference is the OMRA QLDWN Symposium for Studies on Lasting Involvement in Design, Informatics, and Science. The short name of the conference is VANTAGE. The conference is an academic research conference on equity, diversity, and inclusion in computing, attended by faculty researchers from universities across the US. <br/><br/>Our website is at http://vantage2020.qldwn-example.org. <br/><br/>We typically use the colors purple and white, but are open to other colors being integrated into the design. I attached some previous (terrible) logos just so that you can get an idea of what information we've felt it is important to convey and the color scheme. I would prefer to have something more impactful/graphic in a design.<br/><br/>We prefer clean designs with geometric shapes, and with graphic interest.

Target Market(s)

academic researchers, professors, computer scientists, social scientists, those interested in diversity, equity, and inclusion

Logo Text

VANTAGE

Font styles to use
Sans Serif

Colors
6b449b
33a6d7

Requirements
Must have
• The logo must have the short name of the conference, which is VANTAGE
Nice to have
• The full name of the conference is:
• OMRA QLDWN Symposium for Studies on Fairness and Lasting Involvement in Design, Informatics, and Science (VANTAGE)
• It would be nice to work something in that either includes the words "research on equity and inclusion in computing" or some graphic that captures that concept.
Should not have
• Please don't use 1's and 0's to represent computing - we want to dispel that stereotype.

```html
<!DOCTYPE html>
<html lang="en">
<head>
<meta charset="utf-8">
<title>VANTAGE Conference Banner</title>
<link rel="stylesheet" href="https://fonts.googleapis.com/css2?family=Michroma&family=Tenor+Sans&display=swap">
<style>
  :root {
    --page-bg: #e4e4e7;
    --deep-purple: #47287f;
    --lavender: #b39bd0;
    --lavender-soft: #c7b4df;
    --white: #ffffff;
    --rule: #8a74b8;
    --photo-blue: #3f5596;
    --photo-violet: #a68cc6;
    --photo-warm: #c98b72;
  }
  html, body {
    margin: 0;
    width: 1200px;
    height: 1003px;
    overflow: hidden;
    background: var(--page-bg);
  }
  .stage {
    width: 1200px;
    height: 1003px;
    display: flex;
    align-items: center;
    justify-content: center;
  }
  .banner {
    width: 380px;
    height: 950px;
    display: block;
    box-shadow: 0 6px 24px rgba(0,0,0,0.25);
  }
  .banner-title {
    font-family: "Michroma", sans-serif;
    fill: var(--white);
  }
  .banner-fullname {
    font-family: "Tenor Sans", sans-serif;
    fill: var(--white);
  }
  .banner-tagline {
    font-family: "Tenor Sans", sans-serif;
    fill: var(--lavender-soft);
    letter-spacing: 0.3px;
  }
  .banner-url {
    font-family: "Tenor Sans", sans-serif;
    fill: var(--white);
  }
</style>
</head>
<body>
<main class="stage">
  <svg class="banner" viewBox="0 0 542 1355" xmlns="http://www.w3.org/2000/svg">
    <defs>
      <linearGradient id="photoTone" x1="0" y1="0" x2="1" y2="1">
        <stop offset="0" stop-color="var(--photo-blue)"/>
        <stop offset="0.45" stop-color="var(--photo-violet)"/>
        <stop offset="1" stop-color="var(--photo-warm)"/>
      </linearGradient>
    </defs>

    <!-- header visual -->
    <rect class="header-visual" x="0" y="0" width="542" height="780" fill="url(#photoTone)"
          role="img" aria-label="Upward view of glass office towers overlaid with white line icons of computers, devices, gears and people learning"/>

    <!-- stepped diagonal accent band -->
    <polygon class="edge-accent" fill="var(--lavender)"
      points="0,492 150,580 160,606 372,700 425,695 542,748 542,790 0,790"/>
    <polygon class="edge-white" fill="var(--white)"
      points="0,512 152,598 162,622 374,716 425,711 542,764 542,790 0,790"/>

    <!-- main purple field -->
    <polygon class="main-field" fill="var(--deep-purple)"
      points="0,528 153,614 163,640 375,734 425,729 542,780 542,1252 0,1252"/>

    <!-- guide lines -->
    <line x1="50" y1="805" x2="50" y2="1170" stroke="var(--rule)" stroke-width="1.2"/>
    <line x1="10" y1="945" x2="515" y2="945" stroke="var(--rule)" stroke-width="1.2"/>
    <line x1="10" y1="1063" x2="515" y2="1063" stroke="var(--rule)" stroke-width="1.2"/>
    <circle cx="50" cy="945" r="2" fill="var(--lavender)"/>
    <circle cx="50" cy="1063" r="2" fill="var(--lavender)"/>

    <!-- conference name -->
    <text class="banner-title" x="70" y="903" font-size="58" textLength="440" lengthAdjust="spacingAndGlyphs">VANTAGE</text>

    <text class="banner-fullname" font-size="21">
      <tspan x="70" y="998">Studies on Lasting Involvement in</tspan>
      <tspan x="70" y="1026">Design, Informatics, and Science</tspan>
    </text>

    <text class="banner-tagline" x="70" y="1108" font-size="14.5" textLength="441" lengthAdjust="spacingAndGlyphs">RESEARCH ON EQUITY AND INCLUSION IN COMPUTING</text>

    <!-- footer band -->
    <rect x="0" y="1252" width="542" height="8" fill="var(--white)"/>
    <rect x="0" y="1260" width="542" height="95" fill="var(--lavender)"/>
    <polygon class="footer-corner" fill="var(--white)" points="0,1238 132,1355 0,1355"/>

    <text class="banner-url" x="275" y="1308" font-size="19" text-anchor="middle">www.vantage2020.qldwn-example.org</text>
  </svg>
</main>
</body>
</html>
```